Wedding filmmaker needs artistic business card design - brightwaterreels.ca

We are high end wedding filmmakers in a major market who produce cinematic wedding films. We require a business card design that communicates our quality, artistry, and professionalism yet looks progressive and friendly. Colors and design should skew appeal more to the bride-to-be who is usually the decision maker but not be overtly feminine per se. This means generally light pastel shades of ivory, purple, pink, yellow, as examples.
We already have a name logo established: the words "Brightwater Reels" in the font Great Vibes. Designs must use Tallow natural cardstock as the print stock and am leaning heavily toward our name logo in white, but I am open to black as well. Please design any color elements with spot white underneath where possible.
Do not try to compliment or take inspiration from our website design. Treat the card design as a separate stand alone.
Thank you so much for your hard work!

Target Market(s)

Affluent couples spending $50,000+ on their wedding

Industry/Entity Type

Progressive

Contact Information for Business Card

Paul Brightwater
Producer
905-418-2937
www.brightwaterreels.ca
paul@brightwaterreels.ca
twitter @brightwater762

Font styles to use
Serif
Sans Serif

Requirements
Must have
• - Brightwater Reels name logo (reference GIF uploaded for reference only) and catch phrase: Breathtaking wedding films (I'm open to capitalizing all three words, or just first, or all in small caps). I favor logo, and catch phrase on front of card and my contact details on the other side but if you feel strongly about a different design, go for it!
• - Design must be submitted shown on Tallow natural cardstock NOT WHITE cardstock, If you're not familiar with Tallow, this is what it looks like: http://www.quillandtwinejournal.com/wp-content/uploads/2013/07/il_570xN.837264019_kq4m.jpg
Nice to have
• - An original graphic element (eg. movie reel, bouquet, confetti, etc.) that compliments the name logo but is subtle and discreet, doesn't overpower or entangle it.
• -Great use of balance, composition, negative space, etc. I like clean tasteful design
Should not have
• -Lousy boring clip art.
• -Graphic elements, fonts, or color palette from our website
• -White cardstock background
• -designs you have previously submitted for other contests
• -Bold dark colors (eg. red, orange navy blue, etc.)
• -High tech futuristic designs like you'd create for a software company

```html
<!DOCTYPE html>
<html lang="en">
<head>
<meta charset="utf-8">
<title>Brightwater Reels – Business Card</title>
<link rel="stylesheet" href="https://fonts.googleapis.com/css2?family=Alegreya+Sans:wght@300;400;700&display=swap">
<style>
  :root {
    --backdrop: #cdcdcd;
    --tallow: #b8976b;
    --tallow-edge: #ad8c61;
    --ink-white: #ffffff;
    --bloom: #e6d3bb;
  }
  * { margin: 0; padding: 0; box-sizing: border-box; }
  html, body {
    width: 1200px;
    height: 750px;
    overflow: hidden;
    background: var(--backdrop);
  }
  .stage {
    position: relative;
    width: 1200px;
    height: 750px;
    font-family: "Alegreya Sans", "Helvetica Neue", Arial, sans-serif;
    color: var(--ink-white);
  }
  .card {
    position: absolute;
    top: 248px;
    width: 488px;
    height: 276px;
    background: var(--tallow);
    overflow: hidden;
  }
  .card--back { left: 100px; }
  .card--front { left: 615px; }

  /* Contact side */
  .contact-block {
    position: absolute;
    top: 64px;
    left: 0;
    width: 100%;
    text-align: center;
  }
  .person-name {
    font-weight: 300;
    font-size: 21px;
    letter-spacing: 0.3px;
    line-height: 1;
  }
  .person-title {
    margin-top: 6px;
    font-weight: 700;
    font-size: 10px;
    letter-spacing: 3px;
    line-height: 1;
  }
  .contact-list {
    list-style: none;
    margin-top: 30px;
    display: inline-flex;
    flex-direction: column;
    align-items: center;
    gap: 5px;
  }
  .contact-item {
    display: flex;
    align-items: center;
    gap: 7px;
    font-weight: 400;
    font-size: 15.5px;
    line-height: 1.2;
  }
  .contact-icon { width: 13px; height: 13px; flex: none; }
  .social-dot {
    width: 11px; height: 11px; border-radius: 50%;
    background: var(--ink-white); flex: none;
  }

  /* Brand side */
  .brand-block {
    position: absolute;
    top: 86px;
    left: 0;
    width: 100%;
    text-align: center;
  }
  .brand-name {
    font-weight: 400;
    font-size: 38px;
    letter-spacing: 0.5px;
    line-height: 1;
  }
  .brand-tagline {
    margin-top: 6px;
    font-weight: 400;
    font-size: 9.5px;
    letter-spacing: 2px;
    line-height: 1;
  }
  .bloom-cluster {
    position: absolute;
    right: 0;
    bottom: 0;
    width: 330px;
    height: 122px;
  }
</style>
</head>
<body>
<main class="stage">

  <section class="card card--back" aria-label="Business card, contact side">
    <div class="contact-block">
      <h1 class="person-name">Paul Brightwater</h1>
      <p class="person-title">PRODUCER</p>
      <ul class="contact-list">
        <li class="contact-item">
          <svg class="contact-icon" viewBox="0 0 16 16" aria-hidden="true">
            <path fill="#fff" d="M3.6 1.2l2.2-.4 1.4 3.4-1.6 1.2c.8 1.8 2.2 3.2 4 4l1.2-1.6 3.4 1.4-.4 2.2c-.2.9-1 1.6-2 1.5C6.6 12.5 3.5 9.4 2.1 3.2c-.1-1 .6-1.8 1.5-2z"/>
          </svg>
          <span>905-418-2937</span>
        </li>
        <li class="contact-item">
          <svg class="contact-icon" viewBox="0 0 16 16" aria-hidden="true">
            <rect x="1" y="3" width="14" height="10" fill="none" stroke="#fff" stroke-width="1.3"/>
            <path d="M1 3l7 6 7-6" fill="none" stroke="#fff" stroke-width="1.3"/>
          </svg>
          <span>paul@brightwaterreels.ca</span>
        </li>
        <li class="contact-item">
          <svg class="contact-icon" viewBox="0 0 16 16" aria-hidden="true">
            <g fill="none" stroke="#fff" stroke-width="1.2">
              <circle cx="8" cy="8" r="6.5"/>
              <ellipse cx="8" cy="8" rx="2.8" ry="6.5"/>
              <path d="M1.5 8h13M2.5 4.8h11M2.5 11.2h11"/>
            </g>
          </svg>
          <span>www.brightwaterreels.ca</span>
        </li>
        <li class="contact-item">
          <span class="social-dot" aria-hidden="true"></span>
          <span>@brightwater762</span>
        </li>
      </ul>
    </div>
  </section>

  <section class="card card--front" aria-label="Business card, brand side">
    <div class="brand-block">
      <h2 class="brand-name">Brightwater Reels</h2>
      <p class="brand-tagline">BREATHTAKING WEDDING FILMS</p>
    </div>
    <svg class="bloom-cluster" viewBox="0 0 330 122" role="img" aria-label="Cluster of pale roses rising toward the lower right corner">
      <path d="M0 122 C40 110 70 80 120 70 C170 60 200 40 250 22 C285 8 310 0 330 2 L330 122 Z" fill="var(--bloom)" opacity="0.75"/>
    </svg>
  </section>

</main>
</body>
</html>
```